Loomberry AI - Help users create their own recipe for a delicious AI treat!

Our company is an AI startup called Loomberrys. A Loomberry is an easy way to play with data (user can ask questions and get visualized answers about the dataset, sort of like QuillMate). Our users can "bake" their own Loomberrys by combining different sources of data.

We need a page that offers two things (both are required):

(1) TRY A LOOMBERRY --> Present a gallery of pre-made Loomberrys, each of which a user can click on and start playing with inside a popup iFrame. (visually, a Loomberry should be represented by some variation of our logo, attached). Designer does not need to worry about the iFrame popup.

(2) BAKE YOUR OWN LOOMBERRY --> Guide the user through making their own Loomberry recipe. The steps in making a Loomberry are:

A. Pick first ingredient - a Connector that imports the user's own data (visually, we present these options as logos for the Connector source, like Zentor, Pallomix, Brivane KLX, etc.).

B. Pick additional ingredients - the user can choose from 3rd-party cakes to combine with their own data added in (A). (visually, these 3rd-party cake options are presented as "mini" cakes, similar to our logo)

C. Once the ingredients are selected, the user can hit a BAKE button, and an iFrame popup opens, where user can play with the result. Designer does not need to worry about the iFrame popup.

We already have a web page and color scheme that we'd like this page to match (https://www.loomberrys.ai). The designer has freedom to play with format and try variations on the color scheme. The overall design should feel futuristic, fun, but also professional (like our logo).

Target Market(s)

Business users who want an easier way to get answers from large messy data

Industry/Entity Type

Tech/AI

Number of Pages Required

1 page

Font styles to use
Other font styles liked:
• Rubik

Requirements
Must have
• Full page design that matches current website (www.loomberrys.ai) and meets all requirements in the Project Description
Nice to have
• Included in the Project Description
Should not have
• Do not submit any designs that are too cartoonish or would not appeal to a business user

```html
<!DOCTYPE html>
<html lang="en">
<head>
<meta charset="utf-8">
<title>Loomberrys – Try and Bake a Loomberry</title>
<link href="https://fonts.googleapis.com/css2?family=Questrial&display=swap" rel="stylesheet">
<style>
:root{
  --bg:#24304f;
  --bg-deep:#1e2944;
  --footer:#222c48;
  --card:#2d3a5f;
  --field:#1d2743;
  --white:#ffffff;
  --muted:#c9d1e6;
  --yellow:#f8dc4a;
  --pink:#eb7fa0;
  --cyan:#2fd6ea;
  --blue:#1e8fe0;
  --gold:#f3c23a;
}
*{box-sizing:border-box;margin:0;padding:0}
html,body{width:1200px;height:3528px;overflow:hidden}
body{
  position:relative;
  font-family:"Questrial",sans-serif;
  color:var(--white);
  background:
    radial-gradient(ellipse 520px 420px at 600px 1060px,rgba(40,110,190,.55),transparent 70%),
    radial-gradient(ellipse 640px 520px at 140px 1500px,rgba(40,110,190,.45),transparent 70%),
    radial-gradient(ellipse 500px 400px at 1100px 2100px,rgba(40,110,190,.25),transparent 70%),
    var(--bg);
}
.abs{position:absolute}
.wordmark{font-size:34px;letter-spacing:.5px;color:var(--white);display:flex;align-items:center;gap:10px}
.wordmark .mark{width:30px;height:30px;border:2px solid var(--white);border-radius:4px}

/* header */
.site-header .wordmark{left:144px;top:24px}
.nav{top:36px;left:656px;display:flex;font-size:14px;gap:0}
.nav a{color:var(--white);text-decoration:none;position:absolute;white-space:nowrap}
.nav .active{color:var(--gold)}
.nav-divider{left:941px;top:34px;width:2px;height:24px;background:var(--white)}
.login{left:990px;top:36px;font-size:14px;display:flex;align-items:center;gap:10px}

/* hero */
.hero-art{left:75px;top:130px;width:637px;height:460px;border-radius:20px;
  background:radial-gradient(ellipse at 35% 50%,rgba(47,190,240,.55),rgba(40,100,170,.25) 55%,transparent 80%)}
.hero-title{left:612px;top:228px;width:520px;font-size:37px;line-height:40px;font-weight:400}
.hero-sub{left:615px;top:362px;font-size:15px}
.btn{display:flex;align-items:center;justify-content:center;height:39px;border-radius:20px;
  background:linear-gradient(90deg,var(--yellow),var(--pink));color:var(--white);font-size:12px;letter-spacing:.5px;text-transform:uppercase}
.btn-demo{left:615px;top:401px;width:162px}
.btn-waitlist{left:784px;top:401px;width:162px}
.scroll-line{left:599px;top:520px;width:2px;height:108px;background:var(--white)}
.scroll-dot{left:593px;top:626px;width:14px;height:14px;border:2px solid var(--white);border-radius:50%}

.section-title{left:0;width:1200px;text-align:center;font-size:36px}

/* gallery */
.gallery{left:0;top:0}
.gallery text{font-family:"Questrial",sans-serif;fill:#2a3558}

/* steps */
.step{left:144px;width:911px;height:219px;border-radius:40px;border:2px solid transparent;
  background:linear-gradient(var(--card),var(--card)) padding-box,
             linear-gradient(90deg,var(--yellow),var(--pink) 55%,var(--cyan)) border-box}
.step-photo{position:absolute;top:19px;width:283px;height:183px;border-radius:26px}
.step-text{position:absolute;top:0;height:100%;display:flex;flex-direction:column;justify-content:center}
.step-text h3{font-size:24px;font-weight:400;margin-bottom:18px}
.step-text p{font-size:15px;line-height:24px;color:var(--white)}
.step-1{top:1495px}
.step-2{top:1744px}
.step-3{top:1992px}
.step-1 .step-photo,.step-3 .step-photo{left:18px}
.step-1 .step-text,.step-3 .step-text{left:334px;width:540px}
.step-2 .step-photo{right:18px}
.step-2 .step-text{right:334px;width:520px;text-align:right;align-items:flex-end}
.photo-social{background:linear-gradient(135deg,#1d7fd8,#0a4fa8)}
.photo-cake{background:linear-gradient(135deg,#eef0f2,#c8ccd2 60%,#8a6a55)}
.photo-laptop{background:linear-gradient(135deg,#e8ecf0,#b7c2cf 55%,#3b4a66)}

/* faq */
.faq-band{left:0;top:2308px;width:1200px;height:455px;
  background:radial-gradient(ellipse at 50% 60%,rgba(30,50,90,.6),transparent 70%),linear-gradient(180deg,#1c2a4c,#1a2848)}
.faq-item{left:297px;width:603px;border-bottom:2px solid var(--white);font-size:15px;padding-bottom:18px}
.faq-plus{left:879px;width:26px;height:26px;border-radius:50%;background:var(--blue);display:flex;align-items:center;justify-content:center;font-size:18px;line-height:1}

/* contact */
.label{font-size:15px;line-height:25px}
.field{height:53px;background:var(--field);border-radius:3px}
.field-select::after{content:"";position:absolute;right:22px;top:24px;border:5px solid transparent;border-top-color:var(--white)}
.checkline{left:0;width:1200px;top:3208px;text-align:center;font-size:15px}
.checkbox{display:inline-block;width:12px;height:12px;border:1.5px solid var(--white);margin-right:6px;vertical-align:-1px}
.btn-submit{left:519px;top:3248px;width:162px}

/* footer */
.site-footer{left:0;top:3391px;width:1200px;height:137px;background:var(--footer)}
.site-footer .wordmark{left:144px;top:46px}
.copyright{right:144px;top:62px;font-size:13px}
</style>
</head>
<body>

<header class="site-header">
  <div class="abs wordmark"><span class="mark"></span>loomberrys</div>
  <nav class="abs nav">
    <a class="active" style="left:0">Home</a>
    <a style="left:74px">Try Pipo</a>
    <a style="left:174px">About Us</a>
  </nav>
  <div class="abs nav-divider"></div>
  <div class="abs login">
    <svg width="16" height="16" viewBox="0 0 16 16" fill="none" stroke="#fff" stroke-width="1.3"><circle cx="8" cy="5" r="3.2"/><path d="M2 15c0-3.3 2.7-5.5 6-5.5s6 2.2 6 5.5"/></svg>
    Login
  </div>
</header>

<section class="hero">
  <div class="abs hero-art" role="img" aria-label="Glowing birthday cake made of floating data characters"></div>
  <h1 class="abs hero-title">Does your company have data that others would find useful?</h1>
  <p class="abs hero-sub">Our platform helps you monetize insights without exposing raw data</p>
  <div class="abs btn btn-demo">Try web demo</div>
  <div class="abs btn btn-waitlist">Join the waitlist</div>
  <div class="abs scroll-line"></div>
  <div class="abs scroll-dot"></div>
</section>

<section class="try">
  <h2 class="abs section-title" style="top:712px">Try A Loomberry</h2>
  <svg class="abs gallery" width="1200" height="1320" viewBox="0 0 1200 1320">
    <defs>
      <linearGradient id="edge" x1="0" y1="0" x2="1" y2="1">
        <stop offset="0" stop-color="#f8dc4a"/>
        <stop offset=".5" stop-color="#eb7fa0"/>
        <stop offset="1" stop-color="#2fd6ea"/>
      </linearGradient>
    </defs>
    <g fill="#fff" stroke="url(#edge)" stroke-width="3">
      <polygon points="223,811 425,845 427,977 144,1080 144,959"/>
      <polygon points="600,790 722,860 722,986 600,1055 478,986 478,860"/>
      <polygon points="773,845 975,811 1055,959 1055,1080 773,977"/>
      <polygon points="452,1026 574,1096 574,1222 452,1292 330,1222 330,1096"/>
      <polygon points="748,1026 870,1096 870,1222 748,1292 626,1222 626,1096"/>
    </g>
    <g font-size="32" text-anchor="middle">
      <text x="300" y="941">loomberrys</text>
      <text x="600" y="952">loomberrys</text>
      <text x="915" y="941">loomberrys</text>
      <text x="452" y="1190">loomberrys</text>
      <text x="748" y="1190">loomberrys</text>
    </g>
  </svg>
</section>

<section class="bake">
  <h2 class="abs section-title" style="top:1416px">Bake Your Own Loomberry</h2>

  <article class="abs step step-1">
    <div class="step-photo photo-social" role="img" aria-label="Scattered social media app cubes on a blue background"></div>
    <div class="step-text">
      <h3>Pick first ingredient</h3>
      <p>A Connector that imports the user's own data</p>
    </div>
  </article>

  <article class="abs step step-2">
    <div class="step-text">
      <h3>Pick additional ingredients</h3>
      <p>The user can choose from 3rd-party cakes to combine with<br>their own data added in (A)</p>
    </div>
    <div class="step-photo photo-cake" role="img" aria-label="Small chocolate cake on a white plate"></div>
  </article>

  <article class="abs step step-3">
    <div class="step-photo photo-laptop" role="img" aria-label="Laptop showing a data dashboard"></div>
    <div class="step-text">
      <h3>Hit a BAKE button</h3>
      <p>Once the ingredients are selected, the user can hit a BAKE button,<br>and an iFrame popup opens, where the user can play with the result</p>
    </div>
  </article>

  <svg class="abs" style="left:1060px;top:1636px" width="60" height="156" viewBox="0 0 60 156" fill="none" stroke="#fff" stroke-width="1.5">
    <path d="M10 4 C50 20 50 100 16 146" stroke-dasharray="5 4"/>
    <path d="M14 136 L16 146 L25 141"/>
  </svg>
  <svg class="abs" style="left:66px;top:1906px" width="60" height="156" viewBox="0 0 60 156" fill="none" stroke="#fff" stroke-width="1.5">
    <path d="M50 4 C10 20 6 100 44 148" stroke-dasharray="5 4"/>
    <path d="M35 143 L44 148 L45 138"/>
  </svg>
</section>

<section class="faq">
  <div class="abs faq-band" role="img" aria-label="Dark blue circuit board pattern with binary digits"></div>
  <h2 class="abs section-title" style="top:2380px">More Q+A</h2>
  <div class="abs faq-item" style="top:2466px">How does Pipo work if I don't give her my data?</div>
  <div class="abs faq-plus" style="top:2461px">+</div>
  <div class="abs faq-item" style="top:2546px">How is Pipo different than QuillMate?</div>
  <div class="abs faq-plus" style="top:2541px">+</div>
  <div class="abs faq-item" style="top:2626px">How accurate is Pipo?</div>
  <div class="abs faq-plus" style="top:2621px">+</div>
</section>

<section class="contact">
  <h2 class="abs section-title" style="top:2843px">Get In Touch</h2>
  <div class="abs label" style="left:156px;top:2924px">Your name</div>
  <div class="abs label" style="left:467px;top:2924px">Your email</div>
  <div class="abs label" style="left:780px;top:2899px">How would you describe your<br>organization?</div>
  <div class="abs field" style="left:144px;top:2958px;width:288px"></div>
  <div class="abs field" style="left:456px;top:2958px;width:288px"></div>
  <div class="abs field field-select" style="left:768px;top:2958px;width:287px"></div>
  <div class="abs label" style="left:156px;top:3028px">Questions? Feedback? We want it all</div>
  <div class="abs field" style="left:144px;top:3063px;width:911px;height:124px"></div>
  <div class="abs checkline"><span class="checkbox"></span>I'm interested in being an early user / development partner for Pipo</div>
  <div class="abs btn btn-submit">Submit now</div>
</section>

<footer class="abs site-footer">
  <div class="abs wordmark"><span class="mark"></span>loomberrys</div>
  <div class="abs copyright">© Copyrights 2024 | All Rights Reserved</div>
</footer>

</body>
</html>
```